Web Design Project

Please design a new website template for Calderbrook as follows -

Existing Website - http://www.calderbrook.com.au/

Logo - http://rankyoursitenow.com/Design/calderbrook-logo

Navigation - Top Horizontal

Colours: Pink and purple from attached logo (do not use the bright pink from the existing website)

Page Structure: Home, About Us, Services, The Team, Key Contacts, Our Values, Send Resume, Timesheets, Candidates, Clients, Location, Contact Us.

The template should include an enquiry from on all pages with fields: Name, Phone, Email, Enquiry

The template should include their phone number in the top right corner - (08) 9271 5608

It should include a tag line: Temporary & Permanent Support Staff Specialists

The Footer:
Level 5, 7 Pemberly Terrace
SUBIACO
WA 6008
Phone - (08) 9271 5608
Fax - (08) 9271 5690
Email - admin@calderbrook.com.au

Websites they like - http://www.markdunwoodycosmeticclinic.com.au/ (preferably keep the text on a white background on this site)

Include a button/icon for - Job Listings

Home page text - Use what is on their existing website (you can reduce the number of bullet points)

```html
<!DOCTYPE html>
<html lang="en">
<head>
<meta charset="utf-8">
<title>Calderbrook – The Recruitment Bureau</title>
<link rel="stylesheet" href="https://fonts.googleapis.com/css2?family=Signika:wght@300;400;600&family=PT+Sans:ital,wght@0,400;0,700;1,400&display=swap">
<style>
:root{
  --pink:#e54d9c;
  --pink-dark:#d63f8c;
  --pink-light:#f07bb8;
  --purple:#4d1d80;
  --purple-mid:#6a2fa8;
  --purple-bright:#7c3dbd;
  --ink:#222;
  --text:#555;
  --white:#fff;
}
*{box-sizing:border-box;margin:0;padding:0}
html,body{width:960px;height:1200px;overflow:hidden}
body{position:relative;background:var(--white);font-family:"PT Sans",sans-serif;color:var(--text)}

/* header */
.site-header{position:absolute;left:0;top:0;width:960px;height:134px;
  background:linear-gradient(#e85aa5,var(--pink) 30%,var(--pink-dark));border-top:4px solid var(--pink-light)}
.brand-name{position:absolute;left:34px;top:64px;font-family:"Signika",sans-serif;font-weight:400;font-size:27px;letter-spacing:1.5px;color:#1d1020;line-height:1}
.brand-sub{position:absolute;left:76px;top:94px;font-family:"Signika",sans-serif;font-weight:400;font-size:8.5px;letter-spacing:1px;color:#1d1020}
.util-links{position:absolute;right:38px;top:12px;font-family:"Signika",sans-serif;font-weight:300;font-size:12px;color:var(--white)}
.util-links span{margin:0 6px}
.header-phone{position:absolute;right:37px;top:76px;font-family:"Signika",sans-serif;font-weight:300;color:var(--white);font-size:25px;line-height:1}
.header-phone small{font-size:19px;margin-right:10px}

/* nav */
.main-nav{position:absolute;left:0;top:134px;width:960px;height:54px;background:linear-gradient(#fff,#f3f3f3);border-bottom:1px solid #e4e4e4;
  display:flex;padding-left:20px;font-family:"Signika",sans-serif;font-weight:300;font-size:14px;color:#333}
.main-nav a{display:block;line-height:54px;padding:0 15px;color:inherit;text-decoration:none}
.main-nav a.active{background:linear-gradient(var(--purple-bright),var(--purple));color:var(--white)}

/* hero */
.hero{position:absolute;left:0;top:188px;width:960px;height:332px;background:linear-gradient(#fafafa,#ececec)}
.hero-arrow{position:absolute;top:123px;width:38px;height:41px;border:1px solid #cfcfcf;border-radius:3px;background:linear-gradient(#fff,#eee)}
.hero-arrow svg{display:block;margin:13px auto}
.hero-title{position:absolute;left:82px;top:60px;font-family:"Signika",sans-serif;font-weight:600;font-size:30px;color:var(--purple)}
.hero-sub{position:absolute;left:82px;top:100px;font-family:"Signika",sans-serif;font-weight:300;font-size:21px;color:var(--purple)}
.hero-text{position:absolute;left:83px;top:139px;width:355px;font-size:12px;line-height:18.8px;color:#888}
.btn-learn{position:absolute;left:82px;top:226px;width:103px;height:30px;border-radius:3px;background:linear-gradient(var(--purple-bright),var(--purple-mid));
  color:var(--white);font-family:"Signika",sans-serif;font-weight:300;font-size:16px;text-align:center;line-height:29px}
.hero-art{position:absolute;left:455px;top:26px;width:426px;height:278px;
  background:linear-gradient(180deg,rgba(236,236,236,0),rgba(124,70,190,.35) 50%,rgba(236,236,236,0))}

/* welcome */
.welcome{position:absolute;left:31px;top:544px;width:595px}
.welcome h1{font-family:"Signika",sans-serif;font-weight:300;font-size:18px;color:var(--ink);margin-bottom:9px}
.welcome h1 em{font-style:normal;color:var(--purple-mid)}
.welcome p{font-size:10.6px;line-height:16px;color:#444;margin-bottom:15px}
.role-list{position:absolute;top:790px;list-style:none;font-style:italic;font-size:12.3px;color:#555}
.role-list li{height:23.4px;padding-left:12px;position:relative}
.role-list li::before{content:"›";position:absolute;left:0;top:-2px;font-style:normal;color:#999;font-size:14px}

/* enquiry */
.enquiry{position:absolute;left:647px;top:544px;width:286px;height:367px;border:1px solid #d9d9d9;border-radius:5px;background:var(--white)}
.enquiry h2{height:45px;border-radius:5px 5px 0 0;background:linear-gradient(var(--purple-bright),var(--purple));color:var(--white);
  font-family:"Signika",sans-serif;font-weight:300;font-size:17.5px;line-height:45px;padding-left:21px}
.field{position:absolute;left:12px;width:264px;height:31px;border:1px solid #cfcfcf;border-radius:5px;background:var(--white);
  box-shadow:0 3px 4px -2px rgba(0,0,0,.15);font-style:italic;font-size:12px;color:#666;padding:7px 12px}
.field.message{height:124px;padding-top:5px}
.btn-callback{position:absolute;left:14px;top:316px;width:148px;height:36px;border-radius:3px;background:linear-gradient(var(--pink-light),var(--pink-dark));
  color:var(--white);font-family:"Signika",sans-serif;font-weight:300;font-size:16px;text-align:center;line-height:36px}

/* footer */
.site-footer{position:absolute;left:0;top:934px;width:960px;height:266px;background:linear-gradient(#55237f,#7338b2);color:var(--white)}
.foot-col{position:absolute;top:24px;list-style:none;font-family:"Signika",sans-serif;font-size:12px}
.foot-col li{height:30px;line-height:26px;border-bottom:1px solid rgba(255,255,255,.18);width:115px}
.foot-col li:last-child{border-bottom:none}
.job-btn{position:absolute;left:504px;top:22px;width:176px;height:54px;border-radius:27px;background:linear-gradient(#fff,#e9e9e9);
  box-shadow:0 3px 6px rgba(0,0,0,.3);display:flex;align-items:center;justify-content:center;gap:10px;
  font-family:"Signika",sans-serif;font-size:20px;color:var(--purple)}
.address{position:absolute;left:703px;top:23px;font-size:11.5px;line-height:18.5px}
.address h3{font-family:"Signika",sans-serif;font-weight:300;font-size:16px;margin-bottom:1px}
.address b{display:inline-block;width:41px;font-weight:400}
.address span{font-size:13px}
.foot-rule{position:absolute;left:34px;top:199px;width:892px;border-top:1px solid rgba(255,255,255,.25)}
.copyright{position:absolute;left:41px;top:220px;font-size:11.5px}
</style>
</head>
<body>

<header class="site-header">
  <div class="brand-name">CALDERBROOK</div>
  <div class="brand-sub">THE RECRUITMENT BUREAU</div>
  <div class="util-links">FAQ<span>|</span>Location<span>|</span>Contact</div>
  <div class="header-phone"><small>Phone no.</small>(08) 9271 5608</div>
</header>

<nav class="main-nav">
  <a class="active">Home</a><a>About Us</a><a>Services</a><a>The Team</a><a>Key Contacts</a><a>Our Values</a><a>Send Resume</a><a>Timesheets</a><a>Candidates</a><a>Clients</a>
</nav>

<section class="hero">
  <div class="hero-arrow" style="left:13px"><svg width="10" height="14" viewBox="0 0 10 14"><path d="M8 1 2 7l6 6" fill="none" stroke="#555" stroke-width="2.4"/></svg></div>
  <div class="hero-arrow" style="left:904px"><svg width="10" height="14" viewBox="0 0 10 14"><path d="M2 1l6 6-6 6" fill="none" stroke="#555" stroke-width="2.4"/></svg></div>
  <div class="hero-title">Calderbrook</div>
  <div class="hero-sub">The Recruitment Bureau</div>
  <p class="hero-text">To be the best we know what and how to present beautifully the working of the client’s need and their advantages be highlighted. We act in accordance with the Industry certified processes to deliver the best to our clients all over the world.</p>
  <div class="btn-learn">learn more</div>
  <div class="hero-art" role="img" aria-label="Illustration of a crowd of purple figures with one pink figure standing out"></div>
</section>

<section class="welcome">
  <h1>Welcome to <em>Calderbrook</em> Website Mainpage</h1>
  <p>Brightpath Webworks is a web service company, offering a wide range of services which range from designing and development, that is covering almost all the fields in the best possible way. To be the best we know what and how to present beautifully the working of the client’s need and their advantages be highlighted. We act in accordance with the Industry certified processes to deliver the best to our clients all over the world.</p>
  <p>Thus, Wanna get ahead in the competition with other websites. Brightpath Webworks provide you with an attractive and most convincing website to enhance your marketing goals.</p>
  <p>The only way to success is through the right path and that’s what we provide you. None of the other companies has the result we do. So stick to the best that’s how you will be the best don’t opt for the second best. Our expertise does not limit itself to web development but also it includes Web Hosting, Search Engine Optimization, E-Commerce. We partner hundreds of organization to enhance their business, marketing and profit goals.</p>
</section>
<ul class="role-list" style="left:39px"><li>Administration</li><li>Personal Assistant</li><li>Executive Assistant</li><li>Reception</li><li>Secretaries</li></ul>
<ul class="role-list" style="left:181px"><li>Accounts Clerk</li><li>Project Engineering</li><li>Construction and Property</li><li>Accounting</li><li>Customer Service</li></ul>
<ul class="role-list" style="left:369px"><li>Legal</li><li>Data Entry</li><li>Cell Centre</li><li>Project Engineering</li></ul>

<aside class="enquiry">
  <h2>Fill Our Contact Form</h2>
  <div class="field" style="top:55px">type your name</div>
  <div class="field" style="top:99px">type your phone no.</div>
  <div class="field" style="top:138px">type your email address</div>
  <div class="field message" style="top:179px">message</div>
  <div class="btn-callback">Request a Call Back</div>
</aside>

<footer class="site-footer">
  <ul class="foot-col" style="left:44px"><li>Home</li><li>About Us</li><li>Services</li><li>The Team</li><li>Key Contacts</li></ul>
  <ul class="foot-col" style="left:157px"><li>Our Values</li><li>Send Resume</li><li>Timesheets</li><li>Candidates</li><li>Clients</li></ul>
  <ul class="foot-col" style="left:277px"><li>Contact Form</li><li>Location</li><li>FAQ</li><li>Contact</li></ul>
  <ul class="foot-col" style="left:390px"><li>Send Resume</li><li>Candidates</li><li>The Team</li></ul>
  <div class="job-btn">
    <svg width="34" height="30" viewBox="0 0 34 30"><rect x="11" y="2" width="12" height="6" rx="2" fill="none" stroke="#555" stroke-width="2"/><rect x="1" y="7" width="32" height="22" rx="2" fill="#f2a31b"/><rect x="1" y="15" width="32" height="2" fill="#c47c0c"/></svg>
    Job Listings
  </div>
  <div class="address">
    <h3>Calderbrook</h3>
    Level 5, 7 Pemberly Terrace<br>
    SUBIACO&nbsp; WA 6008<br>
    <b>Phone</b><span>(08) 9271 5608</span><br>
    <b>Fax</b><span>(08) 9271 5690</span><br>
    <b>Email</b><span>admin@calderbrook.com.au</span>
  </div>
  <div class="foot-rule"></div>
  <div class="copyright">© 2012 Company Name &nbsp;|&nbsp; All right reserved</div>
</footer>

</body>
</html>
```